Stationery Design for ORVEN

I have now selected the logo for my consultancy company. I need some innovative design for my stationary. The audience is senior executives in international banks predominantly in Asia, but also in the Middle East, Africa and Latin America.
My company advises them on solutions to be able to grow their business.

I will update to a vector file in a few hours
Updates

Target Market(s)

Senior executives in international Banks.

Industry/Entity Type

Business

Requirements
Should not have
• It should not be forgettable!

```html
<!DOCTYPE html>
<html lang="en">
<head>
<meta charset="utf-8">
<title>ORVEN Stationery</title>
<link rel="stylesheet" href="https://fonts.googleapis.com/css2?family=Questrial&family=Arimo:wght@400;700&display=swap">
<style>
  :root {
    --bg: #ececec;
    --paper: #f7f7f7;
    --ink: #3f3f3f;
    --ink-soft: #6a6a6a;
    --rule: #8e8e8e;
    --teal: #3fc7c0;
    --green: #6fe06b;
    --foot-bar: #c4c4c4;
    --sign: #4b5fa8;
  }
  * { box-sizing: border-box; margin: 0; padding: 0; }
  html, body { width: 1200px; height: 815px; overflow: hidden; }
  body { background: var(--bg); position: relative; font-family: "Questrial", "Century Gothic", sans-serif; color: var(--ink); }

  .sheet { position: absolute; top: 70px; width: 484px; height: 685px; background: var(--paper); }
  .sheet--letter { left: 80px; }
  .sheet--fax { left: 638px; }

  .accent-bar { position: absolute; left: 0; top: 52px; width: 12px; height: 48px;
    background: linear-gradient(180deg, var(--teal), var(--green)); }

  .brand { position: absolute; top: 47px; left: 305px; display: flex; align-items: center; gap: 10px; }
  .brand__dot { width: 60px; height: 60px; border-radius: 50%; background: var(--teal); }
  .brand__name { font-size: 21px; letter-spacing: 1px; color: var(--ink-soft); }

  .letter__greeting { position: absolute; left: 63px; top: 177px; font-size: 11.5px; font-weight: 700; font-family: "Arimo", sans-serif; color: #333; }
  .letter__body { position: absolute; left: 63px; top: 229px; width: 384px; }
  .letter__body p { font-size: 7.6px; line-height: 10.8px; text-align: justify; margin-bottom: 10.8px; color: #444; }

  .signature { position: absolute; left: 262px; top: 533px; width: 112px; height: 62px;
    background: linear-gradient(160deg, rgba(75,95,168,0.25), rgba(75,95,168,0.08)); border-radius: 4px; }
  .signoff { position: absolute; right: 38px; top: 542px; text-align: right; }
  .signoff__close { font-size: 7px; color: #555; }
  .signoff__name { font-family: "Arimo", sans-serif; font-weight: 700; font-size: 10px; margin-top: 5px; color: #333; }

  .footer { position: absolute; right: 38px; top: 649px; text-align: right; font-size: 6.3px; line-height: 10px; color: var(--ink-soft); font-family: "Arimo", sans-serif; }
  .footer__label { color: var(--green); font-weight: 700; }
  .footer__web { color: var(--teal); }
  .footer-bar { position: absolute; right: 0; bottom: 0; width: 238px; height: 11px; background: var(--foot-bar); }

  .fax__title { position: absolute; left: 68px; top: 42px; font-family: "Arimo", sans-serif; font-size: 62px; line-height: 1; color: #555; letter-spacing: 1px; }

  .fax-table { position: absolute; left: 23px; top: 151px; width: 437px; border-collapse: collapse; font-family: "Arimo", sans-serif; font-size: 7px; font-weight: 700; color: #444; }
  .fax-table td { border: 1px solid var(--rule); height: 14.5px; padding: 0 5px; }
  .fax-table .label { width: 47px; }
  .fax-table .value { width: 172px; }

  .fax-box { position: absolute; left: 23px; top: 238px; width: 437px; height: 383px; border: 1px solid var(--rule); font-family: "Arimo", sans-serif; }
  .fax-box__flags { display: flex; height: 15px; border-bottom: 1px solid var(--rule); background: #ebebeb; }
  .fax-box__flags span { display: flex; align-items: center; justify-content: center; gap: 4px; font-size: 7px; font-weight: 700; color: #444; border-right: 1px solid var(--rule); }
  .fax-box__flags span:last-child { border-right: none; }
  .fax-box__flags span::before { content: ""; width: 5px; height: 5px; border: 1px solid #666; }
  .fax-box__comments { text-align: center; font-size: 7px; margin-top: 11px; color: #444; }
</style>
</head>
<body>

<section class="sheet sheet--letter">
  <div class="accent-bar"></div>
  <div class="brand"><span class="brand__dot"></span><span class="brand__name">ORVEN</span></div>

  <p class="letter__greeting">Dear sir / madame,</p>
  <div class="letter__body">
    <p>Lorem ipsum dolor sit amet, consectetur adipisicing elit, sed do eiusmod tempor incididunt ut labore et dolore magna aliqua. Ut enim ad minim veniam, quis nostrud exercitation ullamco laboris nisi ut aliquip ex ea commodo consequat. Duis aute irure dolor in reprehenderit in voluptate velit esse cillum dolore eu fugiat nulla pariatur. Excepteur sint occaecat cupidatat non proident, sunt in culpa qui officia deserunt mollit anim id est laborum.Lorem ipsum dolor sit amet, consectetur adipisicing elit, sed do eiusmod tempor incididunt ut labore et dolore magna aliqua. Ut enim ad minim veniam, quis nostrud exercitation ullamco laboris nisi ut aliquip ex ea commodo consequat. Duis aute irure dolor in reprehenderit in voluptate velit esse cillum dolore eu fugiat nulla pariatur. Excepteur sint occaecat cupidatat non proident, sunt in culpa qui officia deserunt mollit anim id est laborum.</p>
    <p>Lorem ipsum dolor sit amet, consectetur adipisicing elit, sed do eiusmod tempor incididunt ut labore et dolore magna aliqua. Ut enim ad minim veniam, quis nostrud exercitation ullamco laboris nisi ut aliquip ex ea commodo consequat. Duis aute irure dolor in reprehenderit in voluptate velit esse cillum dolore eu fugiat nulla pariatur. Excepteur sint occaecat cupidatat non proident, sunt in culpa qui officia deserunt mollit anim id est laborum.</p>
    <p>Lorem ipsum dolor sit amet, consectetur adipisicing elit, sed do eiusmod tempor incididunt ut labore et dolore magna aliqua. Ut enim ad minim veniam, quis nostrud exercitation ullamco laboris nisi ut aliquip ex ea commodo consequat. Duis aute irure dolor in reprehenderit in voluptate velit esse cillum dolore eu fugiat nulla pariatur. Excepteur sint occaecat cupidatat non proident, sunt in culpa qui officia deserunt mollit anim id est laborum.</p>
    <p>Lorem ipsum dolor sit amet, consectetur adipisicing elit, sed do eiusmod tempor incididunt ut labore et dolore magna aliqua. Ut enim ad minim veniam, quis nostrud exercitation ullamco laboris nisi ut aliquip ex ea commodo consequat. Duis aute irure dolor in reprehenderit in voluptate velit esse cillum dolore eu fugiat nulla pariatur. Excepteur sint occaecat cupidatat non proident, sunt in culpa qui officia deserunt mollit anim id est laborum.</p>
  </div>

  <div class="signature" role="img" aria-label="Handwritten signature of the sender"></div>
  <div class="signoff">
    <p class="signoff__close">Yours Sincerely,</p>
    <p class="signoff__name">Lena Corvaith</p>
  </div>

  <div class="footer">
    <p>48 Harlow Lane, 7th Floor West, Springvale, SV 20431</p>
    <p><span class="footer__label">Phone:</span> +555-410-2270 &nbsp;<span class="footer__label">Fax:</span> +555-410-2281 &nbsp;www.<span class="footer__web">orvenadvisory</span>.com</p>
  </div>
  <div class="footer-bar"></div>
</section>

<section class="sheet sheet--fax">
  <div class="accent-bar"></div>
  <h1 class="fax__title">FAX</h1>
  <div class="brand"><span class="brand__dot"></span><span class="brand__name">ORVEN</span></div>

  <table class="fax-table">
    <tr><td class="label">To:</td><td class="value"></td><td class="label">From:</td><td class="value"></td></tr>
    <tr><td class="label">Fax:</td><td class="value"></td><td class="label">Pages:</td><td class="value"></td></tr>
    <tr><td class="label">Phone:</td><td class="value"></td><td class="label">Date:</td><td class="value"></td></tr>
    <tr><td class="label">Re:</td><td class="value"></td><td class="label">CC:</td><td class="value"></td></tr>
  </table>

  <div class="fax-box">
    <div class="fax-box__flags">
      <span style="width:87px">Urgent</span>
      <span style="width:84px">For Review</span>
      <span style="width:97px">Please Comment</span>
      <span style="width:82px">Please Reply</span>
      <span style="width:87px">Confidential</span>
    </div>
    <p class="fax-box__comments">COMMENTS:</p>
  </div>

  <div class="footer">
    <p>48 Harlow Lane, 7th Floor West, Springvale, SV 20431</p>
    <p><span class="footer__label">Phone:</span> +555-410-2270 &nbsp;<span class="footer__label">Fax:</span> +555-410-2281 &nbsp;www.<span class="footer__web">orvenadvisory</span>.com</p>
  </div>
  <div class="footer-bar"></div>
</section>

</body>
</html>
```